Harbourlight Power - Company Brochure / Display Folder / DL Flyer

We are a trader in environmental commodities based in Australia and require the following 4 designs for an upcoming exhibition;
1) Brochure Folder
Essentially this will be a presentation folder for a number of A4 sheets and will allow us to present business cards. We would like it based on the same design as our stand background - please see attached (001) for reference.
I have attached a file (002) that is basically what i am after, if you could recreate this or something similar it be sufficient. Please change the blue lines to green and incorporate an image that represents solar / environment / renewable energy etc.
Please include our logo (003) as well as the words 'experts in environmental commodity trading'
The back of the folder should have our address, contact number, homepage etc - please refer to the website for these details www.harbourlightpower.com.au.
The template is included also, please ensure the deisgn fits within these boundaries for printing (004 / Forme 8)
2) A4 Flyer
We are after a re design of an old flyer that highlights what we do as a business. I have included the wording for this (005) but am open to interpretations as to designs. Please keep it relevant to the graphics requested for the presentation folder.
This will be a single page A4 sheet - very easy.
3) DL Brochure
We will be running a promotion at the exhibition for cash rewards and need a double sided DL flyer designed so the can be handed out. The back of the flyer should have our logo as well as the green graphics consistent with the stand design / background while the front needs to highlight the following promotional offer;
Harbourlight Power Cash Rewards Offer
Get more out of your STC's -trade with us to receive instant cash back!
Trade 1000 STC - receive $250 cash rewards card
Trade 5000 STC - receive $500 cash rewards card
(x1 card on the first 1000 + x2 more cards on the first 5000)
Cash rewards cards are valid everywhere that accepts eftpos - cash can even be withdrawn at ATMS!
Offer valid until October 31st 2014
Unregistered Trade Only.
Please keep this text to the left and incorporate an image or graphic on the right side. One that is professional, ties in with the notion of environmental trading but highlights the offer.
Again we open to interpretations with this one.
4) Card Design
Very basic - a design is needed for the rewards card mentioned in the promotion above. I have attached the template / outline required for this (006/ 007) and basically need out logo and a bit of colour on the cash card.
We are open to some ideas but the main thing is being consistent with the stand design that we will be exhibiting in. We like the graphics used and the plain white with the green curved concept. Please ensure the greens from our logo also.
I will do my best to answer any queries you may have, the files should have all the info needed to get started and we usually have a few design amendments after the first drafts are sent through.
Apologies about the timeframe with this one - we are looking to move fast so the earlier submissions will be considered as I can work back and forth with them.
Good Luck
Harbourlight Power.

```html
<!DOCTYPE html>
<html lang="en">
<head>
<meta charset="utf-8">
<title>Harbourlight Power – Cash Rewards Card</title>
<link href="https://fonts.googleapis.com/css2?family=Questrial&family=PT+Sans+Narrow:wght@400;700&display=swap" rel="stylesheet">
<style>
  :root {
    --backdrop: #dcdcdc;
    --card-white: #ffffff;
    --brand-green: #11713a;
    --mark-green: #8cc63f;
    --wash-light: #eef7e0;
    --wash-mid: #dcefc0;
    --ink: #1d1d1d;
  }
  * { box-sizing: border-box; margin: 0; padding: 0; }
  html, body { width: 1200px; height: 950px; overflow: hidden; }
  body { background: var(--backdrop); position: relative; font-family: "PT Sans Narrow", sans-serif; }

  .card {
    position: absolute;
    top: 226px;
    width: 505px;
    height: 323px;
    border-radius: 24px;
    background: var(--card-white);
    overflow: hidden;
  }
  .card--front { left: 83px; }
  .card--back { left: 627px; }

  .card__wash { position: absolute; inset: 0; }
  .card--front .card__wash {
    background: linear-gradient(165deg, var(--card-white) 0%, var(--card-white) 30%, var(--wash-light) 55%, var(--wash-mid) 78%, var(--wash-light) 100%);
  }
  .card--back .card__wash {
    background: linear-gradient(200deg, var(--wash-light) 0%, var(--wash-mid) 30%, var(--wash-light) 52%, var(--card-white) 75%);
  }

  .card__rule {
    position: absolute;
    left: 0;
    right: 0;
    top: 216px;
    height: 6px;
    background: var(--brand-green);
  }

  .brand {
    position: absolute;
    left: 84px;
    top: 132px;
    display: flex;
    align-items: center;
  }
  .brand__mark {
    width: 48px;
    height: 48px;
    background: var(--mark-green);
    margin-right: 16px;
    flex: none;
  }
  .brand__name {
    font-family: "Questrial", sans-serif;
    font-size: 33px;
    color: var(--brand-green);
    white-space: nowrap;
  }

  .card-value {
    position: absolute;
    right: 26px;
    top: 262px;
    font-weight: 700;
    font-size: 16px;
    color: var(--ink);
  }

  .contact-list {
    position: absolute;
    left: 67px;
    top: 226px;
    list-style: none;
    font-size: 15px;
    color: var(--ink);
  }
  .contact-list li { display: flex; align-items: center; height: 25px; }
  .contact-list svg { width: 13px; height: 13px; margin-right: 9px; flex: none; fill: var(--brand-green); }
</style>
</head>
<body>

<section class="card card--front" aria-label="Card front">
  <div class="card__wash" role="img" aria-label="Soft green flowing wave background"></div>
  <div class="card__rule"></div>
  <div class="brand">
    <span class="brand__mark" aria-hidden="true"></span>
    <span class="brand__name">Harbourlight Power</span>
  </div>
  <div class="card-value">Value $250</div>
</section>

<section class="card card--back" aria-label="Card back">
  <div class="card__wash" role="img" aria-label="Soft green flowing wave background"></div>
  <div class="card__rule"></div>
  <ul class="contact-list">
    <li><svg viewBox="0 0 14 14" aria-hidden="true"><path d="M7 1 L13 7 H11 V13 H8.5 V9 H5.5 V13 H3 V7 H1 Z"/></svg>Level 12 48 Harbour Road, Brisbane 4000 QLD</li>
    <li><svg viewBox="0 0 14 14" aria-hidden="true"><path d="M1 5 C1 2 13 2 13 5 L10.5 6 L9.5 4.5 H4.5 L3.5 6 Z M3 7 H11 L12 12 H2 Z"/></svg>1300 555 214</li>
    <li><svg viewBox="0 0 14 14" aria-hidden="true"><circle cx="7" cy="7" r="6"/></svg>www.harbourlightpower.com.au</li>
  </ul>
</section>

</body>
</html>
```